Collectible Card Trading Company ~ Tidewell and Finch Collectibles

Business card design using the attached images as a reference point. The color pallet is the color choice I prefer. If you have any way of improving on the design that would be appreciated. This will be used as an insert for product shipments as well as at geekfair and other collectible trade shows so it needs to be eye catching and memorable. Anything that you can do to make my business POP with this business card would be appreciated.

Target Market(s)

Collectible card purchasers primarily but all collectors ingeneral

Industry/Entity Type

Retail

Contact Information for Business Card

Details are included on the provided images

Colors

Designer to choose colors to be used in the design.

Requirements
Must have
• Bold design
Nice to have
• N/A
Should not have
• N/A

```html
<!DOCTYPE html>
<html lang="en">
<head>
<meta charset="utf-8">
<title>Tidewell and Finch Collectibles – Business Card</title>
<link href="https://fonts.googleapis.com/css2?family=Oswald:wght@600&family=Lato:wght@400&display=swap" rel="stylesheet">
<style>
  :root {
    --backdrop: #1f1f21;
    --card: #2f333b;
    --gold: #c58a3f;
    --ink: #eceae6;
    --rule: #b9b9b9;
  }
  html, body {
    margin: 0;
    width: 1200px;
    height: 900px;
    overflow: hidden;
    background: var(--backdrop);
  }
  .canvas {
    position: relative;
    width: 1200px;
    height: 900px;
  }
  .card {
    position: absolute;
    width: 640px;
    height: 366px;
    background: var(--card);
    border-radius: 28px;
    box-shadow: 0 18px 40px rgba(0,0,0,.55);
    overflow: hidden;
  }
  .card--front { left: 110px; top: 60px; }
  .card--back  { left: 450px; top: 474px; }

  .brand {
    position: absolute;
    display: flex;
    flex-direction: column;
    align-items: center;
    gap: 14px;
  }
  .card--front .brand {
    left: 0; right: 0; top: 88px;
  }
  .card--back .brand {
    left: 10px; width: 240px; top: 108px;
  }
  .brand__dot {
    width: 84px;
    height: 84px;
    border-radius: 50%;
    background: var(--gold);
  }
  .card--back .brand__dot { width: 60px; height: 60px; }
  .brand__name {
    font-family: "Oswald", sans-serif;
    font-weight: 600;
    color: var(--gold);
    font-size: 34px;
    line-height: 1.1;
    text-align: center;
    letter-spacing: .5px;
  }
  .card--back .brand__name { font-size: 22px; }

  .divider {
    position: absolute;
    left: 262px;
    top: 62px;
    width: 1px;
    height: 240px;
    background: var(--rule);
  }
  .details {
    position: absolute;
    left: 286px;
    top: 58px;
    right: 24px;
    font-family: "Lato", sans-serif;
    color: var(--ink);
  }
  .person__name {
    margin: 0;
    color: var(--gold);
    font-size: 25px;
    font-weight: 400;
    line-height: 1.05;
  }
  .person__title {
    margin: 0 0 22px;
    font-size: 19px;
  }
  .contact {
    list-style: none;
    margin: 0 0 18px;
    padding: 0;
  }
  .contact li {
    display: flex;
    align-items: center;
    gap: 8px;
    font-size: 14px;
    line-height: 22px;
    white-space: nowrap;
  }
  .contact svg { flex: none; width: 15px; height: 15px; }
  .badge {
    flex: none;
    width: 14px;
    height: 14px;
    border-radius: 3px;
    background: var(--gold);
  }
</style>
</head>
<body>
<main class="canvas">

  <section class="card card--front" aria-label="Card front">
    <div class="brand">
      <span class="brand__dot"></span>
      <span class="brand__name">Tidewell and Finch Collectibles</span>
    </div>
  </section>

  <section class="card card--back" aria-label="Card back">
    <div class="brand">
      <span class="brand__dot"></span>
      <span class="brand__name">Tidewell and Finch Collectibles</span>
    </div>

    <span class="divider"></span>

    <div class="details">
      <h1 class="person__name">Marcus Delane Jr.</h1>
      <p class="person__title">Chief Collector</p>

      <ul class="contact">
        <li>
          <svg viewBox="0 0 16 16" aria-hidden="true"><path d="M8 1a5 5 0 0 0-5 5c0 4 5 9 5 9s5-5 5-9a5 5 0 0 0-5-5zm0 7a2 2 0 1 1 0-4 2 2 0 0 1 0 4z" fill="var(--gold)"/></svg>
          harrow creek, oregon
        </li>
        <li>
          <svg viewBox="0 0 16 16" aria-hidden="true"><rect x="1" y="3" width="14" height="10" rx="1.5" fill="var(--gold)"/><path d="M1.5 4l6.5 5 6.5-5" stroke="var(--card)" stroke-width="1.3" fill="none"/></svg>
          marcus@tidewellfinch.com
        </li>
      </ul>

      <ul class="contact">
        <li>
          <svg viewBox="0 0 16 16" aria-hidden="true"><circle cx="8" cy="8" r="6.5" fill="none" stroke="var(--gold)" stroke-width="1.5"/><path d="M1.5 8h13M8 1.5c-2.5 3-2.5 10 0 13M8 1.5c2.5 3 2.5 10 0 13" stroke="var(--gold)" stroke-width="1.2" fill="none"/></svg>
          www.tidewellfinch.com
        </li>
        <li><span class="badge"></span>photos@tidewellfinch</li>
        <li><span class="badge"></span>posts@Tidewell_finch</li>
        <li><span class="badge"></span>shop@www.cardhub.com/store/tidewellfinch</li>
      </ul>
    </div>
  </section>

</main>
</body>
</html>
```